Harlow Stonefield Civil Construction website design

We want a Bold website to promote our Heavy Civil Construction company, We would like an organic / tangible feel to the site. The pictures will be over saturated so they pop. We need to be able to easliy upload new projects and pictures on a regular basis.
Home page will have a full screen width image, "home page image" with silhouette and logo. It will also have about us area and picture
Page 2 will be Project Gallery with pictures in project folders
Page 3 will be an employment application form and submission
Page 4 will be Contact Us
Target Market(s)
Construction indusrty
Industry/Entity Type
Contractor
Coding
Coded - Design and coding required
Number of Pages Required
4 page
Font styles to use
Other font styles liked:
- Hypatia Sans Pro Light
Look and feel

```html
<!DOCTYPE html>
<html lang="en">
<head>
<meta charset="utf-8">
<title>Harlow Stonefield Civil Construction</title>
<link rel="stylesheet" href="https://fonts.googleapis.com/css2?family=Montserrat:wght@400;500;600;700&family=Open+Sans:wght@400;600&display=swap">
<style>
:root{
  --blue:#3957c2;
  --blue-deep:#2d46a3;
  --blue-soft:rgba(57,87,194,.82);
  --ink:#2b2b2b;
  --text:#555a63;
  --muted:#8a8f98;
  --slate:#5d6f78;
  --white:#ffffff;
  --line:#e3e5ea;
}
*{box-sizing:border-box;margin:0;padding:0}
html,body{width:1200px;height:5322px;overflow:hidden}
body{position:relative;background:var(--white);font-family:"Open Sans",Arial,sans-serif;color:var(--text)}
.abs{position:absolute}
.heading{font-family:"Montserrat",Arial,sans-serif;font-weight:600;letter-spacing:2px;text-transform:uppercase}
.section-title{position:absolute;left:0;width:1200px;display:flex;justify-content:center;align-items:center;gap:14px;font-family:"Montserrat",Arial,sans-serif;font-size:20px;letter-spacing:2px;text-transform:uppercase;color:var(--blue)}
.section-title .mark{width:30px;height:30px;border:3px solid var(--blue)}
.section-title .light{color:var(--muted);font-weight:500}
.section-title b{font-weight:600}
.on-blue{color:var(--white)}
.on-blue .mark{border-color:var(--white)}
.btn{position:absolute;display:flex;align-items:center;justify-content:space-between;padding:0 8px 0 18px;height:38px;border-radius:19px;background:var(--blue);color:var(--white);font-family:"Montserrat",Arial,sans-serif;font-size:12px;font-weight:600}
.btn .arrow{width:24px;height:24px;border-radius:50%;border:2px solid var(--white);display:flex;align-items:center;justify-content:center}
.photo{position:absolute}

/* hero */
.hero{position:absolute;left:0;top:0;width:1200px;height:660px;background:linear-gradient(180deg,#9fb2bb 0%,#7d909a 40%,#55656e 75%,#3c4449 100%)}
.brand{position:absolute;left:225px;top:290px;display:flex;align-items:center;gap:22px}
.brand .square{width:120px;height:120px;border:6px solid #1f2326}
.brand .name{font-family:"Montserrat",Arial,sans-serif;font-weight:600;color:#1f2326;font-size:54px;line-height:1;letter-spacing:1px}
.brand .name span{display:block;font-size:35px;letter-spacing:9px;margin-top:12px}
.nav{position:absolute;left:0;top:475px;width:1200px;display:flex;justify-content:center;gap:34px;font-family:"Montserrat",Arial,sans-serif;font-size:13px;letter-spacing:1px;color:#e8ecef;text-transform:uppercase}
.nav a{color:inherit;text-decoration:none;display:flex;align-items:center;gap:7px}
.nav a .ico{width:14px;height:12px;border:1.5px solid currentColor}
.nav a.current{font-weight:700;color:var(--white)}

/* why band */
.why-title{position:absolute;left:0;top:745px;width:1200px;text-align:center;font-family:"Montserrat",Arial,sans-serif;font-weight:700;font-size:24px;color:var(--white)}
.why{position:absolute;top:780px;width:146px;height:146px;border-radius:50%;background:radial-gradient(circle at 40% 35%,#5b7ae0,var(--blue-deep));border:6px solid #bfc8d6;box-shadow:0 0 0 3px #3b3f44;display:flex;flex-direction:column;align-items:center;justify-content:center;gap:10px;color:var(--white);font-size:11px;font-weight:600;text-align:center;line-height:1.2}
.why svg{width:38px;height:38px}

/* about */
.about-text{position:absolute;left:588px;top:1245px;width:570px;font-size:13px;line-height:1.62;color:var(--text)}

/* services */
.service{position:absolute;top:1590px;width:600px;height:386px}
.service .band{position:absolute;left:0;bottom:0;width:100%;height:100px;background:var(--blue-soft);padding:22px 34px;color:var(--white)}
.service h3{font-family:"Montserrat",Arial,sans-serif;font-size:15px;font-weight:600;letter-spacing:1px;margin-bottom:4px}
.service p{font-size:12.5px;line-height:1.5}
.service .badge{position:absolute;right:0;top:88px;width:108px;height:112px;background:var(--blue-soft);display:flex;align-items:center;justify-content:center}

/* projects */
.project{position:absolute;top:2242px;width:442px;height:400px;background:var(--white);box-shadow:0 4px 14px rgba(0,0,0,.14);border-bottom:4px solid var(--blue)}
.project .tag{position:absolute;right:0;top:0;width:0;height:0;border-top:120px solid var(--blue);border-left:120px solid transparent}
.project .tag-text{position:absolute;right:10px;top:14px;width:60px;text-align:center;color:var(--white);font-size:11px;font-weight:600;line-height:1.4}
.project .tag-text i{display:block;margin:0 auto 4px;width:22px;height:22px;border:2px solid var(--white);border-radius:50%}
.project h4{position:absolute;left:22px;top:290px;font-family:"Montserrat",Arial,sans-serif;font-size:14px;font-weight:600;letter-spacing:2px;color:var(--blue)}
.project p{position:absolute;left:22px;top:320px;width:400px;font-size:12.5px;line-height:1.55}
.pager{position:absolute;top:2428px;width:28px;height:28px;border-radius:50%;background:#c9ccd2;display:flex;align-items:center;justify-content:center}

/* testimonials */
.testimonials{position:absolute;left:0;top:2828px;width:1200px;height:612px;background:linear-gradient(120deg,#5574d4 0%,#3957c2 45%,#4a68cc 100%);clip-path:polygon(0 0,100% 0,100% 92%,50% 100%,0 92%)}
.quote{position:absolute;top:3082px;width:312px;height:170px;background:rgba(37,58,140,.55);padding:18px 20px 0 56px;color:var(--white);font-size:13px;line-height:1.5}
.quote .qm{position:absolute;left:18px;top:12px;font-family:Georgia,serif;font-size:44px;font-weight:700;line-height:1}
.quote .avatar{position:absolute;right:14px;bottom:-36px;width:86px;height:86px;border-radius:50%;background:linear-gradient(#e7e9ee,#c8ccd4);border:4px solid var(--white)}
.reviewer{position:absolute;top:3270px;color:var(--white);font-size:14px;font-style:italic;font-weight:600}
.dots{position:absolute;left:570px;top:3342px;display:flex;gap:6px}
.dots i{width:9px;height:9px;border-radius:50%;border:1.5px solid var(--white)}
.dots i.on{background:var(--white)}

/* news */
.news{position:absolute;top:3697px;width:352px}
.news .pic{height:162px}
.news h4{margin-top:24px;text-align:center;font-family:"Montserrat",Arial,sans-serif;font-size:14px;font-weight:600;letter-spacing:1px;color:var(--blue)}
.news p{margin:10px 24px 0;text-align:center;font-size:12px;line-height:1.55}

/* contact */
.contact{position:absolute;left:0;top:4123px;width:1200px;height:640px;background:linear-gradient(160deg,#4a68cc,#3957c2 60%,#3350b8);clip-path:polygon(0 0,50% 5%,100% 0,100% 100%,0 100%)}
.contact .sub{position:absolute;left:0;top:4376px;width:1200px;text-align:center;font-family:"Montserrat",Arial,sans-serif;font-size:13px;font-weight:600;color:var(--white);letter-spacing:1px}
.field{position:absolute;background:rgba(28,46,115,.6);color:var(--white);font-size:12.5px;font-weight:600;padding:12px 14px}
.submit{position:absolute;left:484px;top:4634px;width:232px;height:36px;border:2px solid var(--white);border-radius:18px;color:var(--white);font-family:"Montserrat",Arial,sans-serif;font-size:12px;font-weight:600;display:flex;align-items:center;justify-content:center;letter-spacing:1px}

/* footer */
.foot-brand{position:absolute;left:0;top:4880px;width:1200px;display:flex;justify-content:center;align-items:center;gap:14px}
.foot-brand .square{width:48px;height:48px;border:4px solid var(--blue)}
.foot-brand .name{font-family:"Montserrat",Arial,sans-serif;font-weight:500;color:var(--blue);font-size:22px;line-height:1;letter-spacing:1px}
.foot-brand .name span{display:block;font-size:13px;letter-spacing:4px;margin-top:4px}
.col{position:absolute;top:5012px;font-size:12px;line-height:1.6;color:#3a3f48}
.col h5{font-family:"Montserrat",Arial,sans-serif;font-size:12px;font-weight:700;color:var(--blue);letter-spacing:1px;margin-bottom:18px}
.col li{list-style:none}
.social{display:flex;gap:6px}
.social i{width:22px;height:22px;border-radius:50%;border:1.5px solid #6a6f78}
.newsletter{display:flex;height:30px}
.newsletter .input{width:150px;border:1.5px solid var(--blue);font-size:11px;padding:6px 8px;color:#3a3f48}
.newsletter .go{width:70px;background:var(--blue);color:var(--white);font-size:11px;font-weight:700;display:flex;align-items:center;justify-content:center}
.copyright{position:absolute;left:0;top:5298px;width:1200px;height:24px;background:var(--blue);color:var(--white);font-size:10px;font-weight:600;display:flex;align-items:center;justify-content:center;letter-spacing:.5px}
</style>
</head>
<body>

<!-- HERO -->
<header class="hero">
  <div class="photo" role="img" aria-label="Overcast sky over a construction site with the silhouette of an excavator and dump truck" style="left:0;top:0;width:1200px;height:660px;background:radial-gradient(ellipse at 50% 85%,#2a2f33 0%,rgba(42,47,51,0) 35%),linear-gradient(180deg,rgba(255,255,255,.08),rgba(0,0,0,0))"></div>
  <div class="brand">
    <div class="square"></div>
    <div class="name">HARLOW STONEFIELD<span>CIVIL CONSTRUCTION</span></div>
  </div>
  <nav class="nav">
    <a class="current" href="#"><i class="ico"></i>Home</a>
    <a href="#"><i class="ico"></i>About</a>
    <a href="#"><i class="ico"></i>Services</a>
    <a href="#"><i class="ico"></i>Projects</a>
    <a href="#"><i class="ico"></i>Testimonials</a>
    <a href="#"><i class="ico"></i>Blog</a>
    <a href="#"><i class="ico"></i>Contact</a>
  </nav>
</header>

<svg class="abs" style="left:0;top:650px" width="1200" height="420" viewBox="0 0 1200 420" aria-hidden="true">
  <polygon points="0,0 1200,0 1200,335 600,400 0,335" fill="#2b2b2b"/>
</svg>

<h2 class="why-title">WHY HARLOW STONEFIELD CIVIL CONSTRUCTION</h2>
<div class="why" style="left:182px">
  <svg viewBox="0 0 38 38" fill="none" stroke="#fff" stroke-width="2"><circle cx="19" cy="13" r="7"/><path d="M6 35c0-8 6-12 13-12s13 4 13 12"/></svg>
  Highly<br>Professional
</div>
<div class="why" style="left:414px">
  <svg viewBox="0 0 38 38" fill="none" stroke="#fff" stroke-width="2"><rect x="6" y="6" width="26" height="26"/><path d="M6 16h26M16 16v16"/></svg>
  High Quality<br>Workmanship
</div>
<div class="why" style="left:645px">
  <svg viewBox="0 0 38 38" fill="none" stroke="#fff" stroke-width="2"><path d="M8 20l7 7 15-16"/></svg>
  Quality<br>Services
</div>
<div class="why" style="left:875px">
  <svg viewBox="0 0 38 38" fill="none" stroke="#fff" stroke-width="2"><circle cx="19" cy="19" r="12"/><circle cx="19" cy="19" r="5"/></svg>
  Committed to<br>Excellence
</div>

<!-- ABOUT -->
<div class="photo" role="img" aria-label="Three construction workers in hard hats and orange overalls holding plans and tools" style="left:27px;top:960px;width:492px;height:600px;background:linear-gradient(180deg,#f2c23a 0%,#d98a2a 30%,#c77524 70%,#e9e0d0 100%);border-radius:40% 40% 6px 6px / 14% 14% 6px 6px"></div>
<div class="section-title" style="left:585px;width:auto;top:1160px;justify-content:flex-start"><i class="mark"></i><b>About</b><span class="light">Harlow Stonefield</span></div>
<p class="about-text">Lorem ipsum dolor sit amet, consectetuer adipiscing elit, sed diam nonummy nibh euismod tincidunt ut laoreet dolore magna aliquam erat volutpat. Ut wisi enim ad minim veniam, quis nostrud exerci tation ullamcorper suscipit lobortis nisl ut aliquip ex ea commodo consequat. Duis autem vel eum iriure dolor in hendrerit in vulputate velit esse molestie consequat, vel illum dolore eu feugiat nulla facilisis at vero eros et accumsan et iusto odio dignissim qui blandit praesent luptatum zzril delenit augue duis dolore te feugait nulla facilisi. Nam liber tempor cum soluta nobis eleifend option congue nihil imperdiet.</p>
<div class="btn" style="left:588px;top:1452px;width:230px">Learn More<span class="arrow"><svg width="10" height="10" viewBox="0 0 10 10"><path d="M1 9L9 1M4 1h5v5" stroke="#fff" stroke-width="1.6" fill="none"/></svg></span></div>

<!-- SERVICES -->
<section class="service" style="left:0;clip-path:polygon(0 6%,100% 0,100% 100%,0 100%)">
  <div class="photo" role="img" aria-label="Aerial view of a land development site with a pond and graded lots" style="inset:0;background:linear-gradient(135deg,#7f8f7a,#4f6a57 45%,#9aa392)"></div>
  <div class="badge"><svg width="56" height="44" viewBox="0 0 56 44" fill="none" stroke="#fff" stroke-width="2.5"><rect x="4" y="22" width="34" height="12"/><path d="M38 26h10v8H38M14 22V12h14l6 10"/><circle cx="12" cy="38" r="4"/><circle cx="34" cy="38" r="4"/></svg></div>
  <div class="band"><h3>LAND DEVELOPMENT</h3><p>Lorem ipsum dolor sit amet, consectetuer adipiscing elit, sed diam nonummy nibh euismod tincidunt ut laoreet dolore magna aliquam erat volutpat.</p></div>
</section>
<section class="service" style="left:600px;clip-path:polygon(0 0,100% 6%,100% 100%,0 100%)">
  <div class="photo" role="img" aria-label="Worker in a trench installing underground utility pipe" style="inset:0;background:linear-gradient(160deg,#8a7a62,#b59a5a 40%,#6e5d45)"></div>
  <div class="badge"><svg width="44" height="50" viewBox="0 0 44 50" fill="none" stroke="#fff" stroke-width="2.5"><path d="M22 4v42M6 46L22 4l16 42M10 30h24M14 20h16"/></svg></div>
  <div class="band"><h3>UNDERGROUND UTILITIES</h3><p>Lorem ipsum dolor sit amet, consectetuer adipiscing elit, sed diam nonummy nibh euismod tincidunt ut laoreet dolore magna aliquam erat volutpat.</p></div>
</section>

<!-- PROJECTS -->
<div class="section-title" style="top:2148px"><i class="mark"></i><b>Featured</b><span class="light">Projects</span></div>
<div class="pager" style="left:64px"><svg width="10" height="10" viewBox="0 0 10 10"><path d="M7 1L3 5l4 4" stroke="#fff" stroke-width="2" fill="none"/></svg></div>
<div class="pager" style="left:1108px"><svg width="10" height="10" viewBox="0 0 10 10"><path d="M3 1l4 4-4 4" stroke="#fff" stroke-width="2" fill="none"/></svg></div>
<article class="project" style="left:138px">
  <div class="photo" role="img" aria-label="Bridge construction over a river with a yellow excavator" style="left:0;top:0;width:442px;height:258px;background:linear-gradient(180deg,#bcd4e6 0%,#9bb8cc 45%,#6d7f6c 70%,#4f6673 100%)"></div>
  <div class="tag"></div><div class="tag-text"><i></i>More Info</div>
  <h4>PROJECT #1</h4>
  <p>Lorem ipsum dolor sit amet, consectetuer adipiscing elit, sed diam nonummy nibh euismod tincidunt ut laoreet dolore magna aliquam erat volutpat.</p>
</article>
<article class="project" style="left:617px">
  <div class="photo" role="img" aria-label="Aerial view of a new road cut through dense forest" style="left:0;top:0;width:442px;height:258px;background:linear-gradient(150deg,#3f6b3a,#2e5230 50%,#6d8a5f)"></div>
  <div class="tag"></div><div class="tag-text"><i></i>More Info</div>
  <h4>PROJECT #2</h4>
  <p>Lorem ipsum dolor sit amet, consectetuer adipiscing elit, sed diam nonummy nibh euismod tincidunt ut laoreet dolore magna aliquam erat volutpat.</p>
</article>
<div class="btn" style="left:484px;top:2692px;width:232px">View All<span class="arrow"><svg width="10" height="10" viewBox="0 0 10 10"><path d="M1 9L9 1M4 1h5v5" stroke="#fff" stroke-width="1.6" fill="none"/></svg></span></div>

<!-- TESTIMONIALS -->
<section class="testimonials" role="img" aria-label="Blue tinted photo of engineers reviewing blueprints"></section>
<div class="section-title on-blue" style="top:2990px"><i class="mark"></i><b>Client Testimonials</b></div>
<div class="quote" style="left:88px"><span class="qm">&ldquo;</span>Lorem ipsum dolor sit amet, consectetuer adipiscing elit, sed diam nonummy nibh euismod tincidunt ut laoreet dolore magna aliquam erat volu. Wisi enim ad minim. &rdquo;<span class="avatar" role="img" aria-label="Client portrait"></span></div>
<div class="quote" style="left:439px"><span class="qm">&ldquo;</span>Lorem ipsum dolor sit amet, consectetuer adipiscing elit, sed diam nonummy nibh euismod tincidunt ut laoreet dolore magna aliquam erat volu. Wisi enim ad minim. &rdquo;<span class="avatar" role="img" aria-label="Client portrait"></span></div>
<div class="quote" style="left:790px"><span class="qm">&ldquo;</span>Lorem ipsum dolor sit amet, consectetuer adipiscing elit, sed diam nonummy nibh euismod tincidunt ut laoreet dolore magna aliquam erat volu. Wisi enim ad minim. &rdquo;<span class="avatar" role="img" aria-label="Client portrait"></span></div>
<span class="reviewer" style="left:90px">Marion Castell</span>
<span class="reviewer" style="left:441px">Dana Frey</span>
<span class="reviewer" style="left:792px">Oliver Brandt</span>
<div class="dots"><i class="on"></i><i></i><i></i><i></i></div>

<!-- NEWS -->
<div class="section-title" style="top:3612px"><i class="mark"></i><b>Latest</b><span class="light">News</span></div>
<article class="news" style="left:64px">
  <div class="pic" role="img" aria-label="Workers on a site among steel rebar" style="background:linear-gradient(135deg,#c6823a,#7a5a3a 50%,#d9a85c)"></div>
  <h4>News Title #1</h4>
  <p>Lorem ipsum dolor sit amet, consectetuer adipiscing elit, sed diam nonummy nibh euismod tincidunt ut laoreet dolore magna aliquam.</p>
</article>
<article class="news" style="left:426px">
  <div class="pic" role="img" aria-label="Team meeting around a table seen from above" style="background:linear-gradient(135deg,#3c4148,#8f959c 50%,#4a5058)"></div>
  <h4>News Title #2</h4>
  <p>Lorem ipsum dolor sit amet, consectetuer adipiscing elit, sed diam nonummy nibh euismod tincidunt ut laoreet dolore magna aliquam.</p>
</article>
<article class="news" style="left:787px">
  <div class="pic" role="img" aria-label="Group of business people in an office" style="background:linear-gradient(135deg,#dfe6ee,#7d92ae 50%,#c8d2de)"></div>
  <h4>News Title #3</h4>
  <p>Lorem ipsum dolor sit amet, consectetuer adipiscing elit, sed diam nonummy nibh euismod tincidunt ut laoreet dolore magna aliquam.</p>
</article>
<div class="btn" style="left:148px;top:3992px;width:184px">Read More<span class="arrow"><svg width="10" height="10" viewBox="0 0 10 10"><path d="M1 9L9 1M4 1h5v5" stroke="#fff" stroke-width="1.6" fill="none"/></svg></span></div>
<div class="btn" style="left:508px;top:3992px;width:184px">Read More<span class="arrow"><svg width="10" height="10" viewBox="0 0 10 10"><path d="M1 9L9 1M4 1h5v5" stroke="#fff" stroke-width="1.6" fill="none"/></svg></span></div>
<div class="btn" style="left:869px;top:3992px;width:184px">Read More<span class="arrow"><svg width="10" height="10" viewBox="0 0 10 10"><path d="M1 9L9 1M4 1h5v5" stroke="#fff" stroke-width="1.6" fill="none"/></svg></span></div>

<!-- CONTACT -->
<section class="contact" role="img" aria-label="Blue tinted photo of hands over construction drawings"></section>
<div class="section-title on-blue" style="top:4286px"><i class="mark"></i><b>Contact Us</b></div>
<p class="sub">LET US KNOW WHAT YOU NEED</p>
<div class="field" style="left:116px;top:4424px;width:312px;height:44px">Your Name</div>
<div class="field" style="left:444px;top:4424px;width:312px;height:44px">Your Email</div>
<div class="field" style="left:772px;top:4424px;width:312px;height:44px">Your Subject</div>
<div class="field" style="left:116px;top:4486px;width:968px;height:128px">Message</div>
<div class="submit">SUBMIT</div>

<!-- FOOTER -->
<div class="foot-brand"><i class="square"></i><div class="name">HARLOW STONEFIELD<span>CIVIL CONSTRUCTION</span></div></div>

<div class="col" style="left:82px">
  <h5>QUICK LINKS</h5>
  <ul><li>Home</li><li>About</li><li>Services</li><li>Projects</li><li>Testimonials</li><li>Blog</li><li>Contact</li></ul>
</div>
<div class="col" style="left:238px">
  <h5>SERVICES</h5>
  <ul><li>Land Development</li><li>Underground Utilities</li><li>Excavation and Grading</li><li>Channel Stabilization</li><li>Marine Construction</li></ul>
</div>
<div class="col" style="left:438px">
  <h5>CONTACT</h5>
  <ul>
    <li style="display:flex;gap:8px"><svg width="14" height="14" viewBox="0 0 14 14" fill="none" stroke="#3a3f48" stroke-width="1.4"><path d="M7 13s4.5-4.5 4.5-7.5a4.5 4.5 0 0 0-9 0C2.5 8.5 7 13 7 13z"/><circle cx="7" cy="5.5" r="1.5"/></svg><span>Harlow Stonefield Civil Construction<br>48 Quarry Lane<br>Suite 210<br>Albany, NY 12207</span></li>
    <li style="display:flex;gap:8px;margin-top:6px"><svg width="14" height="14" viewBox="0 0 14 14" fill="none" stroke="#3a3f48" stroke-width="1.4"><path d="M3 1.5h2.5l1.2 3-1.6 1a7 7 0 0 0 3.4 3.4l1-1.6 3 1.2V11a1.5 1.5 0 0 1-1.5 1.5A10 10 0 0 1 1.5 3 1.5 1.5 0 0 1 3 1.5z"/></svg>(518) 555-0142</li>
    <li style="display:flex;gap:8px;margin-top:14px"><svg width="14" height="14" viewBox="0 0 14 14" fill="none" stroke="#3a3f48" stroke-width="1.4"><circle cx="7" cy="7" r="5.5"/><path d="M4 5l3 2.5L10 5"/></svg>info@harlowstonefield.com</li>
  </ul>
</div>
<div class="col" style="left:716px">
  <h5>FOLLOW US</h5>
  <div class="social"><i></i><i></i><i></i></div>
</div>
<div class="col" style="left:864px">
  <h5>NEWSLETTER</h5>
  <div class="newsletter"><div class="input">Enter Email Address</div><div class="go">SIGN UP</div></div>
</div>

<div class="copyright">COPYRIGHT &copy; 2019 HARLOW STONEFIELD CIVIL CONSTRUCTION. ALL RIGHTS RESERVED.</div>

</body>
</html>
```